Stationery for Auditing Firm
Varma Kiran Dinesh & Co
Project: Stationery for Auditing Firm
Stationery for Auditing Firm - Financial Services
Creative Brief
Simple
Vikram T Joshi
Partner
#278/4, Lotus Nivas, 2nd Main 9th Cross, Basavangudi, Bengaluru - 560004
vtj@vkdtax.org
www.vkdtax.org
Need space for a QR code in the front and in the back of the business card
Varma Kiran Dinesh & Co Chartered Accountants
Rachid2014 Rachid2014
I will create more ideas for the envelope and letterheads please wait
ok I will create Letterheads and envelopes please wait
harshadpatel harshadpatel
Need designs for Letterheads and envelopes too
Logo and other files added
Are you have logo Please add your logo

```html
<!DOCTYPE html>
<html lang="en">
<head>
<meta charset="utf-8">
<title>Varma Kiran Dinesh &amp; Co — Stationery</title>
<link rel="stylesheet" href="https://fonts.googleapis.com/css2?family=Montserrat:wght@600;700&family=Open+Sans:wght@400;600;700&display=swap">
<style>
  :root{
    --navy:#1d3e66;
    --green:#7cc242;
    --paper:#ffffff;
    --ink:#4a4f57;
    --muted:#8a9099;
    --placeholder:#d9dde2;
    --backdrop:#e8e8e8;
  }
  *{box-sizing:border-box;margin:0;padding:0}
  html,body{width:1200px;height:881px;overflow:hidden;background:var(--backdrop)}
  body{position:relative;font-family:"Open Sans",Arial,sans-serif;color:var(--ink)}
  .sheet{position:absolute;background:var(--paper);overflow:hidden;box-shadow:0 2px 6px rgba(0,0,0,.12)}
  .sheet svg.wave{position:absolute;left:0;width:100%;display:block}
  .brand{font-family:"Montserrat",Arial,sans-serif;font-weight:700;color:var(--navy);white-space:nowrap;position:absolute}
  .brand--light{color:var(--paper)}
  .firm-title{position:absolute;font-family:"Montserrat",Arial,sans-serif;font-weight:600;white-space:nowrap}

  /* business card front */
  .card-front{left:101px;top:144px;width:235px;height:149px}
  .card-front .qr-space{position:absolute;right:16px;top:34px;width:24px;height:24px;background:var(--placeholder);border:1px solid #c4c9cf}
  .card-front .person{position:absolute;left:14px;top:52px;font-size:9px;font-weight:700;color:var(--navy)}
  .card-front .role{position:absolute;left:14px;top:64px;font-size:6px;color:var(--muted)}
  .card-front .contacts{position:absolute;left:14px;top:84px;font-size:5.5px;line-height:8.5px;list-style:none}
  .card-front .contacts li::before{content:"";display:inline-block;width:4px;height:4px;border-radius:50%;background:var(--green);margin-right:4px;vertical-align:middle}
  .card-front .address{position:absolute;right:14px;top:84px;width:92px;font-size:5.5px;line-height:8.5px;text-align:right}

  /* business card back */
  .card-back{left:355px;top:144px;width:216px;height:149px}
  .card-back .firm-title{left:96px;top:65px;font-size:6px;line-height:9px;color:var(--navy);padding-left:8px;border-left:1px solid var(--green)}

  /* envelope front */
  .envelope-front{left:101px;top:305px;width:470px;height:228px}
  .envelope-front .address{position:absolute;left:24px;top:132px;font-size:6.5px;line-height:10px;width:120px}

  /* envelope back */
  .envelope-back{left:101px;top:559px;width:470px;height:204px}

  /* letterhead */
  .letterhead{left:602px;top:84px;width:497px;height:744px}
  .letterhead .date{position:absolute;left:42px;top:254px;font-size:8px}
  .letterhead .recipient{position:absolute;left:42px;top:278px;font-size:8px;line-height:11px}
  .letterhead .recipient strong{color:var(--navy)}
  .letterhead .salutation{position:absolute;left:42px;top:340px;font-size:10px;font-weight:700;color:var(--navy)}
  .letterhead .body{position:absolute;left:42px;top:360px;width:412px;font-size:7.5px;line-height:12px;color:var(--muted)}
  .letterhead .body p{margin-bottom:14px;text-align:justify}
  .letterhead .footer-contacts{position:absolute;left:42px;top:648px;list-style:none;font-size:7px;line-height:11px}
  .letterhead .footer-contacts li{display:flex;align-items:center;gap:5px}
  .letterhead .footer-contacts svg{width:7px;height:7px;fill:var(--green)}
  .letterhead .footer-office{position:absolute;left:210px;top:648px;font-size:7px;line-height:11px}
  .letterhead .footer-office strong{color:var(--navy)}
  .letterhead .base-rule{position:absolute;left:0;bottom:26px;width:100%;height:4px;background:var(--green)}
</style>
</head>
<body>

<!-- Business card, front -->
<section class="sheet card-front" aria-label="Business card front">
  <svg class="wave" style="top:0" viewBox="0 0 235 50" preserveAspectRatio="none" height="50">
    <path d="M0 0H235V14C170 34 90 10 0 26Z" fill="var(--navy)"/>
    <path d="M0 26C90 10 170 34 235 14V18C170 40 90 16 0 31Z" fill="var(--green)"/>
  </svg>
  <div class="qr-space" role="img" aria-label="Space reserved for QR code"></div>
  <p class="person">Vikram T Joshi</p>
  <p class="role">Partner</p>
  <ul class="contacts">
    <li>+91 98860 24715</li>
    <li>+91 80 4123 5678</li>
    <li>vtj@vkdtax.org</li>
    <li>www.vkdtax.org</li>
  </ul>
  <p class="address">#278/4, Lotus Nivas, 2nd Main 9th Cross, Basavangudi, Bengaluru - 560004</p>
</section>

<!-- Business card, back -->
<section class="sheet card-back" aria-label="Business card back">
  <svg class="wave" style="top:0" viewBox="0 0 216 40" preserveAspectRatio="none" height="40">
    <path d="M0 0H216V12C150 30 70 6 0 22Z" fill="var(--navy)"/>
    <path d="M0 22C70 6 150 30 216 12V16C150 35 70 12 0 27Z" fill="var(--green)"/>
  </svg>
  <span class="brand" style="left:16px;top:66px;font-size:13px">VKD &amp; Co</span>
  <span class="firm-title">Varma Kiran Dinesh &amp; Co<br>Chartered Accountants</span>
  <svg class="wave" style="bottom:0" viewBox="0 0 216 30" preserveAspectRatio="none" height="30">
    <path d="M0 14C70 30 150 4 216 18V30H0Z" fill="var(--navy)"/>
    <path d="M0 10C70 26 150 0 216 14V18C150 4 70 30 0 14Z" fill="var(--green)"/>
  </svg>
</section>

<!-- Envelope, front -->
<section class="sheet envelope-front" aria-label="Envelope front">
  <svg class="wave" style="top:0" viewBox="0 0 470 80" preserveAspectRatio="none" height="80">
    <path d="M0 0H470V40C330 76 170 18 0 54Z" fill="var(--navy)"/>
    <path d="M0 54C170 18 330 76 470 40V47C330 84 170 26 0 61Z" fill="var(--green)"/>
  </svg>
  <span class="firm-title" style="right:24px;top:22px;font-size:7px;color:var(--paper)">Varma Kiran Dinesh &amp; Co Chartered Accountants</span>
  <span class="brand" style="left:22px;top:88px;font-size:16px">VKD &amp; Co</span>
  <p class="address">#278/4, Lotus Nivas,<br>2nd Main 9th Cross,<br>Basavangudi,<br>Bengaluru - 560004</p>
</section>

<!-- Envelope, back -->
<section class="sheet envelope-back" aria-label="Envelope back">
  <svg class="wave" style="top:0" viewBox="0 0 470 80" preserveAspectRatio="none" height="80">
    <path d="M0 0H470V56C330 80 140 80 0 56Z" fill="var(--navy)"/>
    <path d="M0 56C140 80 330 80 470 56V61C330 86 140 86 0 61Z" fill="var(--green)"/>
  </svg>
  <span class="brand brand--light" style="left:200px;top:30px;font-size:14px">VKD &amp; Co</span>
</section>

<!-- Letterhead -->
<section class="sheet letterhead" aria-label="Letterhead">
  <svg class="wave" style="top:0" viewBox="0 0 497 130" preserveAspectRatio="none" height="130">
    <path d="M0 0H497V52C380 92 180 46 0 78Z" fill="var(--navy)"/>
    <path d="M0 78C180 46 380 92 497 52V60C380 102 180 56 0 87Z" fill="var(--green)"/>
  </svg>
  <span class="firm-title" style="right:34px;top:20px;font-size:7px;line-height:10px;color:var(--paper);text-align:right">Varma Kiran Dinesh &amp; Co<br>Chartered Accountants</span>
  <span class="brand" style="left:38px;top:134px;font-size:22px">VKD &amp; Co</span>

  <p class="date">01 January 2021</p>
  <p class="recipient"><strong>Company</strong> / Pro Ltd<br>PO Box 5555 Block D<br>Sample City Country 0000</p>
  <p class="salutation">Dear Anil Rao,</p>
  <div class="body">
    <p>Lorem ipsum dolor sit amet, consectetur adipiscing elit, sed do eiusmod tempor incididunt ut labore et dolore magna aliqua. Ut enim ad minim veniam, quis nostrud exercitation ullamco laboris nisi ut aliquip ex ea commodo consequat. Duis aute irure dolor in reprehenderit in voluptate velit esse cillum dolore eu fugiat nulla pariatur. Excepteur sint occaecat cupidatat non proident, sunt in culpa qui officia deserunt mollit anim id est laborum. Sed ut perspiciatis unde omnis iste natus error sit voluptatem accusantium doloremque laudantium, totam rem aperiam.</p>
    <p>Lorem ipsum dolor sit amet, consectetur adipiscing elit, sed do eiusmod tempor incididunt ut labore et dolore magna aliqua. Ut enim ad minim veniam, quis nostrud exercitation ullamco laboris nisi ut aliquip ex ea commodo consequat. Duis aute irure dolor in reprehenderit in voluptate velit esse cillum dolore eu fugiat nulla pariatur. Excepteur sint occaecat cupidatat non proident, sunt in culpa qui officia deserunt mollit anim id est laborum. Nemo enim ipsam voluptatem quia voluptas sit aspernatur aut odit aut fugit.</p>
  </div>

  <ul class="footer-contacts">
    <li><svg viewBox="0 0 10 10"><circle cx="5" cy="5" r="5"/></svg>+91 80 4123 5678</li>
    <li><svg viewBox="0 0 10 10"><circle cx="5" cy="5" r="5"/></svg>+91 98860 24715</li>
    <li><svg viewBox="0 0 10 10"><circle cx="5" cy="5" r="5"/></svg>vtj@vkdtax.org</li>
    <li><svg viewBox="0 0 10 10"><circle cx="5" cy="5" r="5"/></svg>www.vkdtax.org</li>
  </ul>
  <p class="footer-office"><strong>Varma Kiran Dinesh &amp; Co</strong><br>#278/4, Lotus Nivas<br>2nd Main 9th Cross, Basavangudi<br>Bengaluru - 560004</p>
  <div class="base-rule"></div>
</section>

</body>
</html>
```